Tinselwick Flyer

Require a flyer for our pet photography business. I have uploaded a very poor attempt I have made at designing one. the size is to be DL and to be one page, but coloured on both sides. I have included the template to which the design is to fit.

Target Market(s)

Pet owners

Font styles to use
Sans Serif

Requirements
Must have
• I have included snap shots from our webdesign. The flyer design should be complimentary to the web design. Please use wording on the flyer front from the files called webscreenshots
Nice to have
• The back: a portfolio of the images on the back side with the logo and the website.
• The front: On the front side we would like a maximum of three photos (different to the ones used on the back) with the writing from the screen shots and the logo.
• check the names of the photos to be put on the flyer, I have called them back and front as appropriate.

```html
<!DOCTYPE html>
<html lang="en">
<head>
<meta charset="utf-8">
<title>Tinselwick Pet Photography – DL Flyer</title>
<link href="https://fonts.googleapis.com/css2?family=Montserrat:ital,wght@0,500;0,700;0,800;1,500&display=swap" rel="stylesheet">
<style>
  :root {
    --brand-red: #e31b23;
    --brand-red-dark: #c8141b;
    --paper: #f4f4f4;
    --ink: #1a1a1a;
    --rule: #9a9a9a;
    --backdrop: #e9e4dc;
  }
  * { box-sizing: border-box; margin: 0; padding: 0; }
  html, body { width: 1200px; height: 844px; overflow: hidden; }
  body {
    background: var(--backdrop);
    font-family: "Montserrat", Arial, sans-serif;
    color: var(--ink);
    position: relative;
  }
  .flyer {
    position: absolute;
    top: 42px;
    width: 362px;
    height: 760px;
    background: var(--paper);
    box-shadow: 0 6px 18px rgba(0,0,0,.18);
    overflow: hidden;
  }
  .flyer--front { left: 190px; }
  .flyer--back { left: 648px; }

  /* Front */
  .red-field {
    position: absolute; left: 0; top: 0; width: 100%; height: 520px;
    background: var(--brand-red);
  }
  .panel {
    position: absolute; background: var(--paper);
    display: flex; flex-direction: column; justify-content: center;
    text-align: center; font-weight: 700; font-size: 12px; line-height: 1.3;
  }
  .panel h2 { font-size: 12px; font-weight: 700; margin-bottom: 8px; }
  .panel--one { left: 110px; top: 70px; width: 252px; height: 90px; padding-left: 70px; }
  .panel--two { left: 0; top: 185px; width: 270px; height: 100px; padding-right: 70px; }
  .panel--three { left: 100px; top: 335px; width: 262px; height: 115px; padding-left: 70px; }
  .photo-circle {
    position: absolute; width: 124px; height: 124px; border-radius: 50%;
    border: 5px solid #fff;
  }
  .photo-circle--cat { left: 48px; top: 33px; background: radial-gradient(circle, #9a8f84 0%, #3a3632 70%, #111 100%); }
  .photo-circle--dog-hat { left: 208px; top: 173px; background: radial-gradient(circle, #e8e6e2 0%, #c9d3dc 70%, #a9b6c2 100%); }
  .photo-circle--hound { left: 38px; top: 318px; background: radial-gradient(circle, #b3753f 0%, #3a2416 60%, #0d0d0d 100%); }
  .note {
    position: absolute; left: 0; top: 462px; width: 100%; text-align: center;
    color: #fff; font-style: italic; font-weight: 500; font-size: 9px; line-height: 1.35; padding: 0 40px;
  }

  /* Shared footer */
  .footer {
    position: absolute; left: 0; bottom: 0; width: 100%; height: 200px;
    display: flex; align-items: center; justify-content: space-between;
    padding: 0 26px;
  }
  .brand { display: flex; flex-direction: column; align-items: center; gap: 8px; }
  .brand__mark { width: 40px; height: 40px; border-radius: 50%; border: 2px solid var(--ink); }
  .brand__name {
    color: var(--brand-red); font-weight: 800; font-size: 20px; line-height: 1.05;
    text-transform: uppercase; text-align: center; letter-spacing: .5px;
  }
  .divider { width: 1px; height: 100px; background: var(--rule); }
  .badge { width: 96px; height: 96px; border-radius: 50%; border: 1px solid #cfcfcf; background: #fff; }

  /* Back */
  .portfolio {
    position: absolute; left: 0; top: 0; width: 100%; height: 510px;
    display: grid; grid-template-columns: 1fr 1fr; grid-template-rows: 160px 180px 170px;
  }
  .portfolio__shot--pug { background: linear-gradient(160deg, #d9c8b6, #a77d55); }
  .portfolio__shot--horse { background: linear-gradient(160deg, #b7c6cf, #6b4b34); }
  .portfolio__shot--lady-cat { background: linear-gradient(160deg, #d8cabd, #7b6a5d); }
  .portfolio__shot--tabby { background: linear-gradient(160deg, #8a6a4e, #cfc7bd); }
  .portfolio__shot--poodle { background: linear-gradient(160deg, #f2d9d3, #e6c2bc); }
  .portfolio__shot--collie { background: linear-gradient(160deg, #8ea45a, #3c4a2a); }
  .web-band {
    position: absolute; left: 0; top: 510px; width: 100%; height: 42px;
    background: var(--brand-red); color: #fff; font-weight: 700; font-size: 13px;
    display: flex; align-items: center; justify-content: center; letter-spacing: .5px;
  }
  .flyer--back .footer { height: 208px; }
</style>
</head>
<body>

  <section class="flyer flyer--front">
    <div class="red-field"></div>

    <div class="panel panel--one"><p>Fun Quirky and Beautiful<br>Pet Photography</p></div>
    <div class="photo-circle photo-circle--cat" role="img" aria-label="Fluffy cat portrait on black"></div>

    <div class="panel panel--two">
      <h2>You Get It All!</h2>
      <p>Beautifully printed<br>photographs on art paper<br>along with the digital files</p>
    </div>
    <div class="photo-circle photo-circle--dog-hat" role="img" aria-label="White dog wearing a knitted hat"></div>

    <div class="panel panel--three">
      <h2>Be At Ease</h2>
      <p>In Studio | In Location | At Home<br>All sessions are available<br>to ensure you and your pet<br>are comfortable</p>
    </div>
    <div class="photo-circle photo-circle--hound" role="img" aria-label="Basset hound leaping on black"></div>

    <p class="note">(Note: At this time all Tinselwick Pet Photography<br>is only available in studio)</p>

    <footer class="footer">
      <div class="brand">
        <span class="brand__mark"></span>
        <span class="brand__name">Tinselwick<br>Pet Photography</span>
      </div>
      <span class="divider"></span>
      <span class="badge"></span>
    </footer>
  </section>

  <section class="flyer flyer--back">
    <div class="portfolio">
      <div class="portfolio__shot--pug" role="img" aria-label="Bulldog portrait"></div>
      <div class="portfolio__shot--horse" role="img" aria-label="Woman with her horse"></div>
      <div class="portfolio__shot--lady-cat" role="img" aria-label="Woman holding her cat"></div>
      <div class="portfolio__shot--tabby" role="img" aria-label="Tabby cat in a wicker chair"></div>
      <div class="portfolio__shot--poodle" role="img" aria-label="White poodle on pink backdrop"></div>
      <div class="portfolio__shot--collie" role="img" aria-label="Woman with her border collie on grass"></div>
    </div>
    <div class="web-band">www.tinselwickpetphotography.com</div>
    <footer class="footer">
      <div class="brand">
        <span class="brand__mark"></span>
        <span class="brand__name">Tinselwick<br>Pet Photography</span>
      </div>
      <span class="divider"></span>
      <span class="badge"></span>
    </footer>
  </section>

</body>
</html>
```